Health and Wellness. I am an energetic, but not over the top, Certified Personal Trainer and Nutriti

I need a flyer, 8.5 x 11, representing my company to be displayed in a Doctor's office that specializes in Pain Medicine. Most, if not all, of these clients experience pain or have some chronic diseases such as high blood pressure, high cholesterol, back pain, joint pain, etc. So the flyer should convey that exercise and nutrition reduce/relieves pain and references some of these ailments. Ideally, the flyer should depict an overweight person exercising with a content, or somewhat content or smiling expression on their face in some part of the flyer. My services cover nutrition and include personal training to where I Ideally train people in their home, equipment permitting, or outside in our local Floridian Parks, and sometimes beaches. This flyer will be in a display case, and the bottom right 8.5 x5 cm will need to be blank, or allow for me to input the back of my business car into it, as I'll have business cards readily available in front of the flyer to be taken. I've included some versions of my logos to be added to the flyer. The other picture is of the flyer holder, with business card area, that this flyer will be presented in. Finally, I've attached a pic of what the back of my business card looks like to be input into that bottom right hand corner. You'll be able to see the area in the bottom right that will display my business cards.
Target Market(s)
People looking for weight loss through Nutrition and Fitness. Those looking to relieve joint and/or back pain or those with Chronic diseases such as high blood pressure, high cholesterol, etc.
Industry/Entity Type
Doctor
Requirements
Must have
- Resemble my Logo's color scheme: Red, Teal, and Grey. Some type of photo of an overweight or slightly overweight person exercising.

```html
<!DOCTYPE html>
<html lang="en">
<head>
<meta charset="utf-8">
<title>Harlow's Fitness – Flyer</title>
<link href="https://fonts.googleapis.com/css2?family=Alfa+Slab+One&family=Anton&family=Cabin:wght@500;600;700&family=Exo+2:ital,wght@1,800&display=swap" rel="stylesheet">
<style>
  :root {
    --page-bg: #ececec;
    --paper: #ffffff;
    --ink: #111111;
    --red: #b3151f;
    --rose: #cd5f66;
    --teal: #1aa59a;
    --teal-light: #5fe3d3;
    --grey: #555555;
    --card-grey: #8a8a8a;
    --yellow: #f5d01e;
    --frame: #8e1a22;
  }
  html, body {
    margin: 0;
    width: 1200px;
    height: 1200px;
    overflow: hidden;
    background: var(--page-bg);
  }
  .flyer {
    position: absolute;
    left: 155px;
    top: 25px;
    width: 890px;
    height: 1150px;
    background: var(--paper);
    outline: 2px solid var(--frame);
    overflow: hidden;
    font-family: "Cabin", sans-serif;
  }
  .flyer-shapes { position: absolute; inset: 0; }
  .tagline {
    position: absolute;
    left: 310px; top: 422px; width: 290px;
    margin: 0;
    font-family: "Exo 2", sans-serif;
    font-style: italic; font-weight: 800;
    font-size: 29px; line-height: 34.5px;
    color: var(--yellow);
    text-align: center;
    text-transform: uppercase;
  }
  .brand-mark {
    position: absolute;
    left: 145px; top: 575px;
    width: 100px; height: 100px;
    border: 6px solid var(--red);
    border-radius: 50%;
    box-sizing: border-box;
  }
  .brand-name {
    position: absolute;
    left: 0; top: 705px; width: 400px;
    margin: 0;
    text-align: center;
    font-family: "Cabin", sans-serif;
    font-weight: 600;
    font-size: 33px;
    letter-spacing: 3px;
    color: var(--grey);
    text-transform: uppercase;
  }
  .services {
    position: absolute;
    left: 50px; top: 829px;
    width: 786px; height: 62px;
    border: 3px solid var(--teal);
    border-radius: 12px;
    box-sizing: border-box;
  }
  .services-title {
    position: absolute;
    left: 50%; top: -32px;
    transform: translateX(-50%);
    margin: 0; padding: 0 12px;
    background: var(--paper);
    font-family: "Alfa Slab One", serif;
    font-weight: 400;
    font-size: 44px; line-height: 52px;
    color: var(--red);
    white-space: nowrap;
    text-transform: uppercase;
  }
  .services-list {
    position: absolute;
    left: 0; right: 0; top: 24px;
    margin: 0;
    text-align: center;
    font-size: 20px; font-weight: 500;
    color: var(--ink);
  }
  .trainer-name {
    position: absolute;
    left: 40px; top: 918px; width: 465px;
    margin: 0;
    text-align: center;
    font-family: "Cabin", sans-serif;
    font-weight: 600;
    font-size: 50px; line-height: 56px;
    color: var(--red);
    text-transform: uppercase;
  }
  .trainer-role {
    position: absolute;
    left: 40px; top: 971px; width: 465px;
    margin: 0;
    text-align: center;
    font-size: 21px; font-weight: 500;
    color: var(--ink);
  }
  .contact {
    position: absolute;
    left: 40px; top: 1003px; width: 465px;
    margin: 0;
    text-align: center;
    font-size: 21px; line-height: 28px;
    font-weight: 600;
    color: var(--ink);
  }
  .contact span { display: block; }
  .contact .email { font-weight: 500; }
  .phone {
    position: absolute;
    left: 40px; top: 1064px; width: 460px;
    margin: 0;
    text-align: center;
    font-family: "Anton", sans-serif;
    font-size: 62px; line-height: 72px;
    letter-spacing: 1px;
    background: linear-gradient(180deg, var(--teal-light), var(--teal));
    -webkit-background-clip: text;
    background-clip: text;
    color: transparent;
  }
</style>
</head>
<body>
<main class="flyer">
  <svg class="flyer-shapes" width="890" height="1150" viewBox="0 0 890 1150" xmlns="http://www.w3.org/2000/svg">
    <defs>
      <linearGradient id="photo-warm" x1="0" y1="0" x2="1" y2="1">
        <stop offset="0" stop-color="#d9c8b6"/>
        <stop offset="0.5" stop-color="#9c6a55"/>
        <stop offset="1" stop-color="#3a2c2a"/>
      </linearGradient>
      <linearGradient id="photo-ball" x1="0" y1="0" x2="0" y2="1">
        <stop offset="0" stop-color="#e7e6e2"/>
        <stop offset="0.5" stop-color="#d98a4f"/>
        <stop offset="1" stop-color="#d7c21e"/>
      </linearGradient>
      <linearGradient id="photo-stretch" x1="0" y1="0" x2="0" y2="1">
        <stop offset="0" stop-color="#e9e6df"/>
        <stop offset="0.55" stop-color="#d9b39a"/>
        <stop offset="1" stop-color="#f09a4a"/>
      </linearGradient>
    </defs>

    <polygon class="photo photo-bike" role="img" aria-label="Photo: woman riding an exercise bike in a gym" points="0,0 650,0 270,512 0,512" fill="url(#photo-warm)"/>
    <polygon class="photo photo-ball" role="img" aria-label="Photo: women exercising on stability balls" points="650,0 890,0 890,117 700,395 330,395" fill="url(#photo-ball)"/>
    <polygon class="photo photo-stretch" role="img" aria-label="Photo: smiling woman stretching on a yoga mat" points="890,117 890,760 440,760" fill="url(#photo-stretch)"/>

    <polygon class="accent-stripe" points="640,0 662,0 282,512 260,512" fill="var(--yellow)" opacity="0.75"/>
    <polygon class="accent-stripe" points="662,0 676,0 296,512 282,512" fill="var(--teal-light)" opacity="0.8"/>

    <rect class="band-dark" x="0" y="512" width="300" height="18" fill="var(--ink)"/>
    <polygon class="tagline-panel" points="300,395 700,395 440,767 280,530 300,512" fill="var(--ink)"/>
    <polygon class="accent-stripe" points="700,395 720,367 890,117 890,140 460,767 440,767" fill="var(--teal)" opacity="0.85"/>
    <polygon class="accent-stripe" points="890,140 890,165 480,767 460,767" fill="var(--yellow)" opacity="0.7"/>
    <rect class="band-dark" x="440" y="760" width="450" height="10" fill="var(--ink)"/>

    <polygon class="band-rose" points="0,532 238,532 226,550 0,550" fill="var(--rose)"/>
    <polygon class="band-rose" points="515,777 890,777 890,795 528,795" fill="var(--rose)"/>

    <polygon class="band-rose" points="590,910 873,910 873,930 570,930" fill="var(--rose)"/>
    <polygon class="band-rose" points="502,970 522,950 522,1062 502,1062" fill="var(--rose)"/>
    <rect class="card-slot" x="522" y="930" width="351" height="205" fill="var(--card-grey)"/>

    <polygon class="phone-band" points="35,1063 522,1063 522,1135 0,1135 0,1100" fill="var(--ink)"/>
  </svg>

  <p class="tagline">Helping<br>you to lose<br>weight, gain<br>muscle, and<br>own<br>the room</p>

  <div class="brand-mark" aria-hidden="true"></div>
  <p class="brand-name">Harlow's Fitness</p>

  <section class="services">
    <h1 class="services-title">Fitness Training</h1>
    <p class="services-list">In Your Home, Online, Parks and Beaches, Bride, Groom, and Bridal Party</p>
  </section>

  <h2 class="trainer-name">Evan Harlow</h2>
  <p class="trainer-role">OWNER/TRAINER</p>
  <p class="contact">
    <span class="web">www.harlowsfitness.com</span>
    <span class="email">harlowsfitness1@mailbox.com</span>
  </p>
  <p class="phone">555-214-7360</p>
</main>
</body>
</html>
```